Online only (mobile devices) 50th Birthday Invitation

Design an online (surprise) 50th Birthday dinner invitation for a female (Dellaphine). It should be elegant and similar to the examples uploaded. Will provide restaurant address details, times and RSVP details to winning designer. Please mock up.
Details should be:
Saturday 12th April 2025
Arrive between 6:30pm and 6:45pm
Restaurant Name
Restaurant Address
RSVP name and mobile phone by Friday 4 April 2025
Target Market(s)
The person's friends and family
Requirements
Must have
- Elegance and class
Nice to have
- Gold or silver colouring

```html
<!DOCTYPE html>
<html lang="en">
<head>
<meta charset="utf-8">
<title>Dellaphine's 50th Birthday Invitation</title>
<link rel="stylesheet" href="https://fonts.googleapis.com/css2?family=Montserrat:wght@500;600&family=Pinyon+Script&family=Playfair+Display:ital@1&display=swap">
<style>
  :root {
    --backdrop: #f4f0e4;
    --card-top: #141b21;
    --card-bottom: #03070a;
    --gold: #e9c590;
    --gold-light: #f0d2a4;
    --gold-deep: #c99a63;
    --frame-line: rgba(214, 178, 128, 0.55);
  }
  * { margin: 0; padding: 0; box-sizing: border-box; }
  html, body {
    width: 947px;
    height: 1200px;
    overflow: hidden;
    background: var(--backdrop);
  }
  .invitation {
    position: absolute;
    left: 153px;
    top: 31px;
    width: 640px;
    height: 1138px;
    background: linear-gradient(180deg, var(--card-top) 0%, #0a1116 45%, var(--card-bottom) 100%);
    color: var(--gold);
    font-family: "Montserrat", sans-serif;
    font-variant: small-caps;
    text-align: center;
  }
  .invitation__frame {
    position: absolute;
    inset: 22px;
    border: 1px solid var(--frame-line);
  }
  .line {
    position: absolute;
    left: 0;
    right: 0;
    line-height: 1;
    font-weight: 600;
    letter-spacing: 0.02em;
  }
  .intro { top: 95px; font-size: 18px; }
  .honoree {
    top: 158px;
    font-family: "Pinyon Script", cursive;
    font-variant: normal;
    font-weight: 400;
    font-size: 46px;
    letter-spacing: 0;
  }
  .gold-dust {
    position: absolute;
    left: 114px;
    top: 500px;
    width: 403px;
    height: 283px;
    background:
      radial-gradient(ellipse 50% 60% at 52% 80%, rgba(176, 136, 82, 0.5) 0%, rgba(120, 92, 56, 0.22) 45%, rgba(0,0,0,0) 75%),
      radial-gradient(ellipse 30% 45% at 58% 25%, rgba(90, 80, 70, 0.3) 0%, rgba(0,0,0,0) 80%);
  }
  .gold-dust__floor {
    position: absolute;
    left: 114px;
    top: 782px;
    width: 403px;
    height: 3px;
    background: linear-gradient(90deg, rgba(200,160,100,0), rgba(200,160,100,0.6), rgba(200,160,100,0));
  }
  .age-mark {
    position: absolute;
    left: 0;
    top: 0;
    width: 640px;
    height: 800px;
    overflow: visible;
  }
  .age-mark__numeral {
    font-family: "Playfair Display", serif;
    font-style: italic;
    font-size: 380px;
  }
  .age-mark__ordinal {
    font-family: "Pinyon Script", cursive;
    font-size: 34px;
    fill: var(--gold);
  }
  .date { top: 830px; font-size: 24px; }
  .detail { font-size: 17px; }
  .arrive-1 { top: 880px; }
  .arrive-2 { top: 902px; }
  .venue-1 { top: 947px; }
  .venue-2 { top: 969px; }
  .rsvp-1 { top: 1014px; }
  .rsvp-2 { top: 1036px; }
  .rsvp-3 { top: 1058px; }
</style>
</head>
<body>
  <main class="invitation">
    <div class="invitation__frame"></div>
    <p class="line intro">Join us to celebrate</p>
    <p class="line honoree">Dellaphine's</p>

    <div class="gold-dust" role="img" aria-label="Burst of scattered gold dust rising from the ground"></div>
    <div class="gold-dust__floor"></div>

    <svg class="age-mark" viewBox="0 0 640 800" aria-label="50th">
      <defs>
        <linearGradient id="gold-foil" x1="0" y1="0" x2="1" y2="1">
          <stop offset="0" stop-color="#f0d2a4"/>
          <stop offset="0.55" stop-color="#c99a63"/>
          <stop offset="1" stop-color="#e9c590"/>
        </linearGradient>
      </defs>
      <text class="age-mark__numeral" x="161" y="565" textLength="182" lengthAdjust="spacingAndGlyphs" fill="url(#gold-foil)">5</text>
      <text class="age-mark__numeral" x="256" y="703" textLength="188" lengthAdjust="spacingAndGlyphs" fill="url(#gold-foil)">0</text>
      <text class="age-mark__ordinal" x="450" y="700">th</text>
    </svg>

    <p class="line date">Saturday 12th April 2025</p>
    <p class="line detail arrive-1">Arrive at</p>
    <p class="line detail arrive-2">6:30pm and 6:45pm</p>
    <p class="line detail venue-1">Restaurant Name</p>
    <p class="line detail venue-2">Restaurant Address</p>
    <p class="line detail rsvp-1">RSVP name and</p>
    <p class="line detail rsvp-2">mobile phone</p>
    <p class="line detail rsvp-3">by Friday 4 April 2025</p>
  </main>
</body>
</html>
```